Business Card for a Child Psychologist

I am a psychologist working with children and families and need a business card to give to clients and referral sources. I see children of all ages, so it should not look too young - as it will be for older children too. My work involves dealing with families in difficult situations, likes divorce, or with issues such as depression and anxiety. The design should communicate that I provide an open,warm, friendly, and caring atmosphere. I want to convey a sense of hope and positivity. Using colors like blues, purples

Target Market(s)

Families, doctors, family law attorneys

Industry/Entity Type

Psychology

Contact Information for Business Card

Lorna Pettigrew, Ph.D.
462 W. Brambleton, Suite 2150
Chicago, Illinois 60688
312-555-0173
drlornampettigrew@quenmail.example

Font styles to use
Script

Requirements
Must have
• A Logo to go with the details of my contact information.
Should not have
• Nothing in the shape of a brain. Nothing sad, or that looks too clinical.

```html
<!DOCTYPE html>
<html lang="en">
<head>
<meta charset="UTF-8">
<title>Lorna Pettigrew, Ph.D. – Business Card</title>
<link rel="stylesheet" href="https://fonts.googleapis.com/css2?family=Sacramento&family=Arimo:wght@700&display=swap">
<style>
  :root {
    --page-bg: #e4e2ee;
    --card-bg: #2f2a63;
    --card-bg-soft: #3b3478;
    --accent: #c9b8ff;
    --accent-light: #e6ddff;
    --accent-blue: #8fc3ff;
    --ink: #2f2a63;
    --card-w: 700px;
    --card-h: 400px;
  }
  * { box-sizing: border-box; margin: 0; padding: 0; }
  html, body {
    width: 1200px; height: 1200px; overflow: hidden;
    background: var(--page-bg);
  }
  .canvas { position: relative; width: 1200px; height: 1200px; }

  .card {
    position: absolute; left: 250px;
    width: var(--card-w); height: var(--card-h);
    background: radial-gradient(circle at 30% 20%, var(--card-bg-soft) 0%, var(--card-bg) 70%);
    border: 7px solid var(--accent);
    overflow: hidden;
  }
  .card--front { top: 150px; }
  .card--back { top: 640px; }

  .brand-mark {
    position: absolute;
    border-radius: 50%;
    background: linear-gradient(135deg, var(--accent-light) 0%, var(--accent) 55%, var(--accent-blue) 100%);
    display: flex; align-items: center; justify-content: center;
    color: var(--ink);
    font-family: 'Arimo', Arial, sans-serif;
    font-weight: 700;
  }
  .card--front .brand-mark {
    width: 140px; height: 140px;
    left: 273px; top: 52px;
    font-size: 21px;
  }
  .card--back .brand-mark {
    width: 96px; height: 96px;
    left: 36px; top: 84px;
    font-size: 14px;
  }

  .holder-name {
    position: absolute;
    font-family: 'Sacramento', cursive;
    font-weight: 400;
    color: var(--accent-light);
    white-space: nowrap;
  }
  .card--front .holder-name {
    left: 0; right: 0; top: 210px;
    text-align: center;
    font-size: 58px;
  }
  .card--back .holder-name {
    left: 160px; top: 76px;
    font-size: 50px;
  }
  .holder-role {
    position: absolute;
    left: 160px; width: 470px; top: 144px;
    text-align: right;
    font-family: 'Arimo', Arial, sans-serif;
    font-weight: 700;
    font-size: 15px;
    color: var(--accent-blue);
  }

  .accent-band {
    position: absolute;
    left: 0; right: 0; top: 196px; height: 12px;
    background: linear-gradient(90deg, transparent 0%, var(--accent) 30%, var(--accent-light) 55%, var(--accent-blue) 78%, transparent 100%);
  }

  .contact-list {
    position: absolute;
    left: 60px; top: 236px;
    list-style: none;
    font-family: 'Arimo', Arial, sans-serif;
    font-weight: 700;
    font-size: 16px;
    color: var(--accent-light);
  }
  .contact-item {
    display: flex; align-items: center; gap: 14px;
    margin-bottom: 10px;
    line-height: 1.2;
  }
  .contact-icon {
    flex: none;
    width: 32px; height: 32px;
    border-radius: 7px;
    background: var(--accent);
    display: flex; align-items: center; justify-content: center;
  }
  .contact-icon svg { width: 20px; height: 20px; }
</style>
</head>
<body>
<main class="canvas">

  <section class="card card--front" aria-label="Card front">
    <div class="brand-mark">Pettigrew</div>
    <h1 class="holder-name">Lorna Pettigrew, Ph.D.</h1>
  </section>

  <section class="card card--back" aria-label="Card back">
    <div class="brand-mark">Pettigrew</div>
    <h2 class="holder-name">Lorna Pettigrew, Ph.D.</h2>
    <p class="holder-role">Psychologist</p>
    <div class="accent-band"></div>

    <ul class="contact-list">
      <li class="contact-item">
        <span class="contact-icon">
          <svg viewBox="0 0 24 24" aria-hidden="true"><path fill="#2f2a63" d="M6.6 10.8a15.1 15.1 0 0 0 6.6 6.6l2.2-2.2c.3-.3.7-.4 1-.2 1.1.4 2.3.6 3.6.6.6 0 1 .4 1 1V20c0 .6-.4 1-1 1A17 17 0 0 1 3 4c0-.6.4-1 1-1h3.5c.6 0 1 .4 1 1 0 1.3.2 2.5.6 3.6.1.3 0 .7-.2 1z"/></svg>
        </span>
        <span>312-555-0173</span>
      </li>
      <li class="contact-item">
        <span class="contact-icon">
          <svg viewBox="0 0 24 24" aria-hidden="true" fill="none" stroke="#2f2a63" stroke-width="2"><circle cx="12" cy="12" r="9"/><path d="M3 12h18M12 3c3 3 3 15 0 18M12 3c-3 3-3 15 0 18"/></svg>
        </span>
        <span>drlornampettigrew@quenmail.example</span>
      </li>
      <li class="contact-item">
        <span class="contact-icon">
          <svg viewBox="0 0 24 24" aria-hidden="true"><path fill="#2f2a63" d="M12 2a7 7 0 0 0-7 7c0 5 7 13 7 13s7-8 7-13a7 7 0 0 0-7-7zm0 9.5A2.5 2.5 0 1 1 12 6.5a2.5 2.5 0 0 1 0 5z"/></svg>
        </span>
        <span>462 W. Brambleton, Suite 2150<br>Chicago, Illinois 60688</span>
      </li>
    </ul>
  </section>

</main>
</body>
</html>
```